Bespoke catering company needs a simple but effective kick ass website

I need a website for a bespoke catering company based in the west side of Melbourne called "plova" by Marcus Pellow, I used the words Food-Dining-Events on my business cards which i still want to maintain through out the site.
My main market is aimed towards, in-house dining experiences of restaurant quality, cocktail food, small weddings / engagements, small events.
I have a plova logo in yellow in Hoefler title font with a black background, so the website design would include yellow and black and still using the Hoefler Titling font.
I want the site map to have 5 drop down bars including Home, About Me, Gallery, Menu, Contact me. It needs to be easy to move around.
I want links to my Facebook page, instagram and twitter.
The site needs to be easy for myself to change on a regular basis due to changing seasonal menus and gallery pictures.
Updates
Hi,
I have just added loads of photos of my food into the brief and adjusted the preferences slightly. Can you please update your submissions using my photos?
Thanks,
Marcus
Target Market(s)
The target market is customers looking for quality ,restaurant style dining and cocktail food in their own home or for their private event.
Industry/Entity Type
Restaurant
Font styles to use
Other font styles liked:
- Hoefler Titling
Look and feel
Each slider illustrates characteristics of the customer's brand and the style your logo design should communicate.

```html
<!DOCTYPE html>
<html lang="en">
<head>
<meta charset="utf-8">
<title>plova — food . events . dining</title>
<link href="https://fonts.googleapis.com/css2?family=Questrial&family=Open+Sans:wght@400;600&display=swap" rel="stylesheet">
<style>
  :root {
    --ink: #1c1c1c;
    --header-top: #272727;
    --header-bottom: #111111;
    --gold: #fdc300;
    --gold-deep: #f5a800;
    --white: #ffffff;
    --text: #4a4a4a;
    --text-soft: #5c5c5c;
    --panel-border: #d6d6d6;
    --footer-bg: #f3f3f3;
    --social-one: #3b5a9a;
    --social-two: #4fb3e6;
    --social-three: #5a4a3e;
  }
  * { margin: 0; padding: 0; box-sizing: border-box; }
  html, body { width: 1096px; height: 1200px; overflow: hidden; background: var(--white); }
  body { position: relative; font-family: "Open Sans", sans-serif; color: var(--text); }

  .masthead {
    position: absolute; left: 0; top: 0; width: 1096px; height: 357px;
    background: linear-gradient(180deg, var(--header-top) 0%, var(--header-bottom) 100%);
  }
  .brand { position: absolute; left: 92px; top: 22px; width: 190px; height: 98px; }
  .brand-name {
    font-family: "Questrial", sans-serif; font-size: 62px; line-height: 1;
    color: var(--white); letter-spacing: 1px;
  }
  .brand-by { position: absolute; left: 82px; top: 70px; font-size: 9px; color: #8a8a8a; }
  .brand-tag { position: absolute; left: 82px; top: 82px; font-size: 10px; color: var(--gold); }

  .main-nav { position: absolute; left: 521px; top: 60px; display: flex; align-items: center; }
  .main-nav a {
    font-family: "Questrial", sans-serif; font-size: 17px; color: var(--white);
    text-decoration: none; padding: 0 16px; line-height: 22px;
    border-left: 1px solid #4a4a4a;
  }
  .main-nav a:nth-child(2) { border-left: none; }
  .main-nav a.is-active {
    border-left: none; background: linear-gradient(180deg, var(--gold) 0%, var(--gold-deep) 100%);
    color: var(--ink); border-radius: 21px; height: 42px; line-height: 42px; padding: 0 22px;
  }

  .hero {
    position: absolute; left: 77px; top: 132px; width: 942px; height: 396px;
    background: var(--white); padding: 7px; box-shadow: 0 6px 12px rgba(0,0,0,0.12);
    border: 1px solid #e2e2e2;
  }
  .hero svg { display: block; }
  .hero-copy { position: absolute; left: 44px; top: 100px; width: 280px; color: var(--ink); }
  .hero-kicker { font-family: "Questrial", sans-serif; font-size: 24px; }
  .hero-title { font-family: "Questrial", sans-serif; font-size: 35px; margin-top: 2px; letter-spacing: 0.5px; }
  .hero-text { color: var(--white); font-weight: 600; font-size: 12.5px; line-height: 20px; margin-top: 4px; width: 245px; }
  .hero-dots { display: flex; gap: 3px; margin-top: 14px; }
  .hero-dots span { width: 14px; height: 14px; border-radius: 50%; background: var(--white); }

  .welcome { position: absolute; left: 110px; top: 560px; width: 876px; text-align: center; }
  .welcome h1 { font-family: "Questrial", sans-serif; font-weight: 400; font-size: 30px; color: var(--ink); letter-spacing: 0.5px; }
  .welcome p { font-size: 11.5px; line-height: 18.5px; color: var(--text-soft); margin-top: 5px; }

  .divider { position: absolute; left: 77px; top: 709px; width: 942px; border-top: 2px dotted #c4c4c4; }

  .panel {
    position: absolute; top: 754px; width: 306px; height: 292px;
    border: 1px solid var(--panel-border); border-radius: 3px;
    background: linear-gradient(180deg, var(--white) 80%, #f2f2f2 100%);
  }
  .panel-menu { left: 77px; }
  .panel-gallery { left: 394px; }
  .panel-why { left: 712px; }
  .panel-head {
    height: 54px; line-height: 54px; text-align: center;
    font-family: "Questrial", sans-serif; font-weight: 400; font-size: 22px; color: var(--ink);
    border-bottom: 1px solid var(--panel-border); letter-spacing: 0.3px;
  }
  .panel-menu .panel-head { background: linear-gradient(180deg, #333 0%, #111 100%); color: var(--white); border-radius: 2px 2px 0 0; }

  .dish-list { list-style: none; margin: 21px 0 0 30px; width: 226px; }
  .dish-list li {
    font-size: 12px; color: var(--text); height: 26px; line-height: 26px; padding-left: 16px;
    border-bottom: 1px solid #e4e4e4; position: relative;
  }
  .dish-list li:last-child { border-bottom: none; }
  .dish-list li::before {
    content: ""; position: absolute; left: 2px; top: 10px; width: 4px; height: 4px;
    border-right: 1px solid #777; border-top: 1px solid #777; transform: rotate(45deg);
  }

  .gallery-grid { display: grid; grid-template-columns: repeat(3, 86px); gap: 13px 8px; margin: 22px 0 0 17px; }
  .gallery-tile { width: 86px; height: 83px; border-radius: 3px; }
  .tile-1 { background: linear-gradient(135deg, #e9d3a5, #c98a3a); }
  .tile-2 { background: linear-gradient(135deg, #7a3a1c, #5b8a2e); }
  .tile-3 { background: linear-gradient(135deg, #c8283a, #f3d9d9); }
  .tile-4 { background: linear-gradient(135deg, #b56a2a, #3f6b22); }
  .tile-5 { background: linear-gradient(135deg, #e8c25a, #c73a22); }
  .tile-6 { background: linear-gradient(135deg, #2a2a2a, #8a5a3a); }

  .why-body { padding: 24px 18px 0 22px; font-size: 11.5px; line-height: 18.4px; color: var(--text-soft); }
  .why-photo { float: left; width: 95px; height: 84px; margin: 2px 10px 4px 0; border-radius: 3px;
    background: linear-gradient(135deg, #d23a3a, #e9b23a 50%, #5a8a3a); }

  .site-footer {
    position: absolute; left: 0; top: 1085px; width: 1096px; height: 115px;
    background: var(--footer-bg); border-top: 1px solid #dedede;
  }
  .footer-nav { position: absolute; left: 81px; top: 27px; font-size: 13.5px; color: var(--ink); }
  .footer-nav a { color: var(--ink); text-decoration: none; }
  .footer-nav .sep { margin: 0 4px; }
  .copyright { position: absolute; left: 81px; top: 54px; font-size: 11.5px; color: var(--text-soft); }
  .social { position: absolute; left: 928px; top: 31px; display: flex; gap: 9px; }
  .social a { width: 24px; height: 24px; border-radius: 3px; display: block; }
  .social-one { background: var(--social-one); }
  .social-two { background: var(--social-two); }
  .social-three { background: var(--social-three); }
</style>
</head>
<body>
  <header class="masthead">
    <div class="brand">
      <div class="brand-name">plova</div>
      <div class="brand-by">by marcus pellow</div>
      <div class="brand-tag">food . events . dining</div>
    </div>
    <nav class="main-nav">
      <a class="is-active" href="#">Home</a>
      <a href="#">About Me</a>
      <a href="#">Gallery</a>
      <a href="#">Menu</a>
      <a href="#">Contact me</a>
    </nav>
  </header>

  <section class="hero">
    <svg width="926" height="380" viewBox="0 0 926 380">
      <defs>
        <linearGradient id="hero-photo-tone" x1="0" y1="0" x2="1" y2="1">
          <stop offset="0" stop-color="#efe4d6"/>
          <stop offset="0.5" stop-color="#c9a176"/>
          <stop offset="1" stop-color="#e8dccd"/>
        </linearGradient>
      </defs>
      <rect x="0" y="0" width="926" height="380" fill="url(#hero-photo-tone)" role="img" aria-label="Platter of mini burger sliders with skewers on a white plate"/>
      <path d="M0 0 H429 Q285 130 261 380 H0 Z" fill="#fdc300"/>
      <path d="M431 0 Q288 131 264 380" fill="none" stroke="#ffffff" stroke-width="4"/>
    </svg>
    <div class="hero-copy">
      <div class="hero-kicker">Experienced &amp; Quality</div>
      <div class="hero-title">Cocktail Food</div>
      <p class="hero-text">Phasellus felis dolor, scelerisque a, tempus eget, lobortis id, libero. Donec scelerisque leo ac risus.</p>
      <div class="hero-dots"><span></span><span></span><span></span><span></span></div>
    </div>
  </section>

  <section class="welcome">
    <h1>Welcome to Our Website Mainpage..</h1>
    <p>Donec scelerisque leo ac risus. Praesent sit amet est. In dictum, dolor eu dictum porttitor, enim felis viverra mi, eget luctus massa purus quis odio. Etiam nulla massa, pharetra facilisis, volutpat in, imperdiet sit amet, sem. Aliquam nec erat at purus cursus interdum.</p>
    <p>Class aptent taciti sociosqu ad litora torquent per conubia nostra, per inceptos hymenaeos. Proin nulla arcu, nonummy luctus, dictum eget, fermentum et, lorem. Nunc porta convallis pede.Vestibulum ligula augue, bibendum accumsan, vestibulum ut, commodo a, mi</p>
  </section>

  <div class="divider"></div>

  <section class="panel panel-menu">
    <h2 class="panel-head">Menu of the Day</h2>
    <ul class="dish-list">
      <li>Facilisis volutpat in imperdiet</li>
      <li>Sit amet sem</li>
      <li>Aliquam nec erat</li>
      <li>Purus cursus interdum</li>
      <li>Class aptent taciti</li>
      <li>Sociosqu ad litora</li>
      <li>Torquent per conubia</li>
    </ul>
  </section>

  <section class="panel panel-gallery">
    <h2 class="panel-head">Our Gallery</h2>
    <div class="gallery-grid">
      <div class="gallery-tile tile-1" role="img" aria-label="Pasta salad with vegetables"></div>
      <div class="gallery-tile tile-2" role="img" aria-label="Glazed roast meat on greens"></div>
      <div class="gallery-tile tile-3" role="img" aria-label="Strawberry desserts with cream"></div>
      <div class="gallery-tile tile-4" role="img" aria-label="Grilled chicken with salad"></div>
      <div class="gallery-tile tile-5" role="img" aria-label="Pasta with tomato and basil"></div>
      <div class="gallery-tile tile-6" role="img" aria-label="Plated salmon dish"></div>
    </div>
  </section>

  <section class="panel panel-why">
    <h2 class="panel-head">Why Choose Us</h2>
    <div class="why-body">
      <div class="why-photo" role="img" aria-label="Colourful vegetable canapés in glasses"></div>
      Donec scelerisque leo ac risus. Praesent sit amet est dictum, dolor eu dictum porttitor, enim felis viverra mi, eget luctus massa purus quis odio massa, pharetra facilisis, volutpat in, imperdiet sit amet, sem. Aliquam nec erat at purus cursus interdum. Class aptent taciti sociosqu ad litora torquent per conubia nostra, per inceptos
    </div>
  </section>

  <footer class="site-footer">
    <nav class="footer-nav">
      <a href="#">Home</a><span class="sep">|</span><a href="#">About Me</a><span class="sep">|</span><a href="#">Gallery</a><span class="sep">|</span><a href="#">Menu</a><span class="sep">|</span><a href="#">Contact me</a>
    </nav>
    <p class="copyright">© 2013 Company Name.&nbsp; All right reserved.&nbsp; Term of Use</p>
    <div class="social">
      <a class="social-one" href="#" aria-label="Social profile one"></a>
      <a class="social-two" href="#" aria-label="Social profile two"></a>
      <a class="social-three" href="#" aria-label="Social profile three"></a>
    </div>
  </footer>
</body>
</html>
```